Q7 Picks High Quality Stainless Steel Professional Guitar Picks

I am releasing a new line of Guitar Picks.
These picks are made of stainless steel with an innovative design and manufacturing process. These Picks are for electric guitar and bass guitar players with a modern look, feel and tone. I need packaging that looks high quality, professional, with a modern feel. I also want them to look almost like a luxury product, "The Valdrenne of guitar picks" luxury but modern and masculine. The packaging itself should show off the product so potential buyers can see the product from inside the packaging while not taking up much retail space when displayed. each package will include a qty of 4 Picks. would be great for product to be seen from the front and back. not closed in a box unless the box has windows for the picks viewable from both sides.

Target Market(s)

Musicians, Electric Bass and guitar players all Genre's of music. all ages, professionals. and semi professionals.

Industry/Entity Type

Steel

Font styles to use
Serif
Sans Serif
Other font styles liked:
• Bank Gothic

Colors

Designer to choose colors to be used in the design.

Requirements
Must have
• packaging to be simple I don't want my cost of packaging to be expensive to produce. If you google guitar pick packaging its very simple its just a small polly bag with a header card stapled over it and it hangs on retail hooks. I want something similar but still unique. I am open to other ideas than the typical hang tag/polybag.
Nice to have
• Just to explain a little further "hopefully this is making sense."
• Starting out I plan on having 3 different size picks with matching packaging plus a sample pack. The different Picks are labeled as
• Standard, Jazz, & Bass.
• Standard picks have a black finish with Orange logo.
• "PMS 151 C" (packaging to match.)
• Jazz picks have a Copper finish with a Silver Logo.
• (packaging to match.)
• Bass picks have a Gun Metal finish with a Teal logo
• "PMS 7465 C" (packaging to match.)
• Sample pack will contain 3 Picks (one of each)
• packaging colors TBD.
Should not have
• a picture or drawing of the product, music notes, pictures or drawings of guitars

```html
<!DOCTYPE html>
<html lang="en">
<head>
<meta charset="utf-8">
<title>Q7 Picks – Sample Pack Header Card</title>
<link href="https://fonts.googleapis.com/css2?family=Saira:wght@400;500&family=Great+Vibes&display=swap" rel="stylesheet">
<style>
  :root {
    --page-bg: #e4e4e4;
    --card-dark: #1c1c1e;
    --card-mid: #3a3a3d;
    --brand-orange: #e8901e;
    --gold-light: #f6d27a;
    --gold-deep: #c07a12;
    --silver-light: #f4f4f4;
    --silver-mid: #b9b9bb;
    --silver-dark: #7d7d80;
    --text-light: #f2f2f2;
    --text-dark: #151515;
    --window-bg: #dcdcdc;
    --pick-copper: #d4a24e;
    --pick-gunmetal: #1f5a4e;
    --pick-sand: #f1e2a6;
  }
  html, body {
    margin: 0;
    padding: 0;
    width: 1200px;
    height: 1172px;
    overflow: hidden;
    background: var(--page-bg);
  }
  .header-card {
    position: absolute;
    left: 210px;
    top: 56px;
    width: 780px;
    height: 1060px;
    border-radius: 34px;
    background:
      repeating-linear-gradient(176deg, rgba(255,255,255,0.035) 0 2px, rgba(0,0,0,0.05) 2px 5px),
      linear-gradient(100deg, var(--card-dark) 0%, var(--card-mid) 45%, var(--card-dark) 100%);
    overflow: hidden;
    font-family: "Saira", sans-serif;
  }
  .brand-name {
    position: absolute;
    left: 56px;
    top: 112px;
    margin: 0;
    font-size: 66px;
    font-weight: 500;
    color: var(--brand-orange);
    letter-spacing: 1px;
    line-height: 1;
  }
  .product-title {
    position: absolute;
    left: 436px;
    top: 48px;
    margin: 0;
    font-size: 42px;
    font-weight: 400;
    line-height: 42px;
    color: var(--text-light);
  }
  .material-badge {
    position: absolute;
    left: 418px;
    top: 168px;
    width: 314px;
    height: 128px;
    box-sizing: border-box;
    border-radius: 64px;
    border: 4px solid var(--silver-light);
    background: linear-gradient(160deg, var(--silver-dark) 0%, var(--silver-light) 40%, var(--silver-mid) 65%, var(--silver-light) 100%);
    box-shadow: 0 0 0 3px var(--silver-dark);
    text-align: center;
    color: var(--text-dark);
    padding-top: 18px;
  }
  .material-badge .badge-main { display: block; font-size: 38px; line-height: 44px; }
  .material-badge .badge-sub { display: block; font-size: 31px; line-height: 36px; font-weight: 500; }
  .pick-window {
    position: absolute;
    left: 36px;
    top: 347px;
    width: 704px;
    height: 704px;
  }
  .size-label {
    position: absolute;
    margin: 0;
    font-family: "Great Vibes", cursive;
    font-size: 52px;
    color: var(--text-light);
    line-height: 1;
    white-space: nowrap;
  }
  .size-label.standard { left: 22px; top: 370px; transform: rotate(-38deg); }
  .size-label.bass { left: 18px; top: 950px; transform: rotate(62deg); }
  .size-label.jazz { left: 628px; top: 950px; transform: rotate(-48deg); }
</style>
</head>
<body>
  <div class="header-card">
    <h1 class="brand-name">Q7 Picks</h1>
    <h2 class="product-title">Professional<br>Guitar Picks</h2>
    <div class="material-badge">
      <span class="badge-main">High Quality</span>
      <span class="badge-sub">Stainless Steel</span>
    </div>

    <p class="size-label standard">Standard</p>
    <p class="size-label bass">Bass</p>
    <p class="size-label jazz">Jazz</p>

    <svg class="pick-window" viewBox="0 0 704 704" xmlns="http://www.w3.org/2000/svg">
      <defs>
        <linearGradient id="gold-ring" x1="0" y1="0" x2="0" y2="1">
          <stop offset="0" stop-color="var(--gold-deep)"/>
          <stop offset="0.5" stop-color="var(--gold-light)"/>
          <stop offset="1" stop-color="var(--gold-deep)"/>
        </linearGradient>
        <radialGradient id="window-fill" cx="0.5" cy="0.45" r="0.6">
          <stop offset="0" stop-color="#efefef"/>
          <stop offset="1" stop-color="#c9c9c9"/>
        </radialGradient>
      </defs>
      <circle cx="352" cy="352" r="344" fill="url(#window-fill)" stroke="url(#gold-ring)" stroke-width="9"/>
      <path role="img" aria-label="Copper finish standard pick" fill="var(--pick-copper)"
        d="M230 70 Q340 40 440 65 Q480 80 455 130 L360 310 Q340 340 320 305 L215 125 Q195 85 230 70 Z"/>
      <path role="img" aria-label="Gunmetal finish bass pick with teal logo" fill="var(--pick-gunmetal)"
        d="M95 300 Q110 280 145 285 Q260 300 340 330 Q375 350 345 380 L170 560 Q140 590 115 555 Q70 460 80 340 Q82 310 95 300 Z"/>
      <path role="img" aria-label="Light gold finish jazz pick" fill="var(--pick-sand)"
        d="M385 360 Q480 320 590 315 Q640 315 630 350 Q605 470 530 560 Q505 590 475 570 L380 420 Q360 380 385 360 Z"/>
    </svg>
  </div>
</body>
</html>
```